Technology Solutions Provider

Let’s design a business card that will be as simple and bold at the same time. Name, email address, website & phone number.

Target Market(s)

Small to Medium Size Business

Industry/Entity Type

It Professional

Contact Information for Business Card

Name, email, website, phone numbers

Font styles to use
Sans Serif

Colors
ec1f27
f04a50
dddddd
919191
000000
ffffff

Requirements
Must have
• Clean simple look using my existing logo. I just need to the basic contact information on this card.
Nice to have
• Im considering the square size card versus the standard size business card.
Should not have
• No Mailing Address, no list of services.

```html
<!DOCTYPE html>
<html lang="en">
<head>
<meta charset="utf-8">
<title>Kora Systems – Business Card</title>
<link rel="stylesheet" href="https://fonts.googleapis.com/css2?family=Archivo:wght@400;600;800&family=Tinos&display=swap">
<style>
  :root {
    --red: #ec1f27;
    --red-soft: #f04a50;
    --light: #dddddd;
    --grey: #919191;
    --black: #000000;
    --white: #ffffff;
    --ink: #2a2a2a;
    --stage: #3a3a3a;
    --card-face: #f4f4f4;
  }
  html, body {
    margin: 0;
    padding: 0;
    width: 1200px;
    height: 751px;
    overflow: hidden;
    background: var(--stage);
  }
  .stage {
    position: relative;
    width: 1200px;
    height: 751px;
  }
  .card {
    position: absolute;
    top: 213px;
    width: 322px;
    height: 322px;
    overflow: hidden;
  }
  .card--front { left: 224px; background: var(--card-face); }
  .card--back { left: 615px; }

  .brand {
    position: absolute;
    display: flex;
    flex-direction: column;
    align-items: flex-end;
  }
  .brand__name {
    display: flex;
    align-items: center;
    gap: 6px;
    font-family: "Archivo", sans-serif;
    font-weight: 600;
    font-size: 27px;
    line-height: 1;
    letter-spacing: 0.5px;
  }
  .brand__dot {
    width: 12px;
    height: 12px;
    border-radius: 50%;
  }
  .brand__tagline {
    font-family: "Tinos", serif;
    font-size: 11.5px;
    margin-top: 2px;
  }
  .card--front .brand { left: 36px; top: 50px; width: 250px; }
  .card--front .brand__name { color: var(--ink); }
  .card--front .brand__dot { background: var(--red); }
  .card--front .brand__tagline { color: var(--grey); }

  .contact {
    position: absolute;
    left: 0;
    right: 0;
    top: 155px;
    text-align: center;
  }
  .contact__name {
    font-family: "Archivo", sans-serif;
    font-weight: 800;
    font-size: 18px;
    color: var(--red);
    margin: 0;
  }
  .contact__role {
    font-family: "Archivo", sans-serif;
    font-weight: 600;
    font-size: 12.5px;
    color: var(--ink);
    margin: 2px 0 8px;
  }
  .contact__line {
    font-family: "Tinos", serif;
    font-size: 14px;
    color: #4a4a4a;
    line-height: 17.5px;
    margin: 0;
  }
  .front-band {
    position: absolute;
    left: 0;
    bottom: 0;
    width: 322px;
    height: 322px;
  }
  .website {
    position: absolute;
    left: 0;
    right: 0;
    bottom: 9px;
    text-align: center;
    font-family: "Archivo", sans-serif;
    font-weight: 600;
    font-size: 11px;
    letter-spacing: 2.6px;
    color: var(--white);
  }

  .back-field {
    position: absolute;
    inset: 0;
    background: var(--red);
  }
  .card--back .brand { left: 32px; top: 140px; width: 280px; }
  .card--back .brand__name { color: var(--white); }
  .card--back .brand__dot { background: var(--white); }
  .card--back .brand__tagline { color: var(--white); }
</style>
</head>
<body>
<main class="stage">
  <section class="card card--front" aria-label="Card front">
    <div class="brand">
      <div class="brand__name"><span class="brand__dot"></span>kora systems</div>
      <div class="brand__tagline">technology solutions provider</div>
    </div>

    <div class="contact">
      <p class="contact__name">ALAN REED</p>
      <p class="contact__role">CEO/Founder</p>
      <p class="contact__line">P. 555 210 4821</p>
      <p class="contact__line">M. 555 374 9016</p>
      <p class="contact__line">alan@korasystems.com</p>
    </div>

    <svg class="front-band" viewBox="0 0 322 322" aria-hidden="true">
      <path d="M0 250 Q161 330 322 250" fill="none" stroke="var(--ink)" stroke-width="2.5"/>
      <path d="M0 258 Q161 334 322 258 L322 322 L0 322 Z" fill="var(--red)"/>
    </svg>
    <div class="website">www.korasystems.com</div>
  </section>

  <section class="card card--back" aria-label="Card back">
    <div class="back-field" role="img" aria-label="Red background with a faint repeating brand-symbol pattern"></div>
    <div class="brand">
      <div class="brand__name"><span class="brand__dot"></span>kora systems</div>
      <div class="brand__tagline">technology solutions provider</div>
    </div>
  </section>
</main>
</body>
</html>
```